Create Bramble Learning Works a card design that will stick in the mind of prospects.

Bramble Learning Works specialises designs and produces training video, animation, illustration and text.

We need a card design that oozes class and leaves the prospect brimming with confidence.

The design will feature the Bramble Learning Works all black logo (uploaded). The design may also use the shade of orange from the orange version of the logo (uploaded). Note, just the color is to be used e.g. for the back of the card, not the orange logo itself.

The Bramble brand is about authenticity, quality, maturity and assurance. We are a safe buy when it comes to the prospects next project.

Target Market(s)

The primary target is training managers or others who are responsible for choosing to hire companies to produce their training media e.g. video. This will usually be a large spend so they need to have confidence.

Industry/Entity Type

Training

Contact Information for Business Card

FRONT:

Bramble Learning Works
Phone: 03 9512 4379
1st Floor, 418 Ferncliff Road
Mt Dellmoor
VIC 3187
Australia
www.bramblelearning.com.au

Lionel Pratt
Founder and Lead Consultant
mobile: +61 3 0452 736 218
email: lionel@bramblelearning.com.au

BACK:
Specialising in design and production of training:

video
animation
illustration
text

for delivery via internet, intranet and/or LMS.

Number of Pages Required

4 page

Font styles to use
Sans Serif

Requirements
Must have
• The black logo uploaded with the brief.
Nice to have
• The inclusion of the shade of orange found in the orange logo also uploaded with the brief. One example would be having the back of the card in this orange and using a white font for the text. But I want the designer to work this out.
Should not have
• No colours other than black and the orange included in the uploaded orange logo.

```html
<!DOCTYPE html>
<html lang="en">
<head>
<meta charset="utf-8">
<title>Bramble Learning Works — Business Card</title>
<link href="https://fonts.googleapis.com/css2?family=Open+Sans:wght@400;600;700&family=Noto+Serif:ital@1&display=swap" rel="stylesheet">
<style>
  :root {
    --backdrop: #b4b4b4;
    --paper: #f7f7f7;
    --ink: #1c1a1b;
    --ink-soft: #3a3738;
    --card-dark: #2b2627;
    --on-dark: #ffffff;
    --on-dark-muted: #d2cfd0;
  }
  * { box-sizing: border-box; margin: 0; padding: 0; }
  html, body { width: 1200px; height: 900px; overflow: hidden; }
  body {
    background: var(--backdrop);
    font-family: "Open Sans", Arial, sans-serif;
    position: relative;
  }
  .card {
    position: absolute;
    top: 297px;
    width: 500px;
    height: 306px;
    box-shadow: 0 6px 18px rgba(0,0,0,0.18);
    overflow: hidden;
  }

  /* Front */
  .card--front { left: 80px; background: var(--paper); color: var(--ink); }
  .person { position: absolute; left: 32px; top: 30px; }
  .person__name { font-size: 18px; font-weight: 700; line-height: 1.2; }
  .person__title { font-size: 12px; color: var(--ink-soft); margin-bottom: 6px; }
  .contact-line {
    display: flex; align-items: center; gap: 7px;
    font-size: 11.5px; color: var(--ink-soft); line-height: 1.6;
  }
  .contact-line svg { width: 10px; height: 10px; flex: none; }
  .brand-name {
    position: absolute; left: 32px; top: 150px;
    font-size: 42px; font-weight: 700; letter-spacing: -0.5px;
    color: var(--ink);
  }
  .company {
    position: absolute; right: 32px; bottom: 28px;
    text-align: right;
  }
  .company__name { font-size: 14px; font-weight: 700; line-height: 1.4; }
  .company__address { font-size: 11.5px; color: var(--ink-soft); line-height: 1.45; margin-bottom: 8px; }
  .company .contact-line { justify-content: flex-end; }

  /* Back */
  .card--back { left: 620px; background: var(--card-dark); color: var(--on-dark); }
  .back__brand {
    position: absolute; right: 60px; top: 44px;
    font-size: 46px; font-weight: 700; letter-spacing: -0.5px;
  }
  .back__tagline {
    position: absolute; right: 30px; top: 122px;
    font-family: "Noto Serif", Georgia, serif; font-style: italic;
    font-size: 13.5px; color: var(--on-dark-muted);
  }
  .back__services {
    position: absolute; right: 30px; top: 150px;
    font-size: 13px; font-weight: 700; word-spacing: 2px;
  }
  .back__delivery {
    position: absolute; right: 30px; top: 196px;
    font-size: 13.5px; font-weight: 700;
  }
  .back__band {
    position: absolute; left: 0; right: 0; top: 228px; height: 20px;
    background: var(--on-dark);
  }
</style>
</head>
<body>

  <section class="card card--front" aria-label="Card front">
    <div class="person">
      <p class="person__name">Lionel Pratt</p>
      <p class="person__title">Founder and Lead Consultant</p>
      <p class="contact-line">
        <svg viewBox="0 0 10 10" aria-hidden="true"><rect x="2" y="0.5" width="6" height="9" rx="1" fill="none" stroke="currentColor" stroke-width="1.2"/></svg>
        +61 3 0452 736 218
      </p>
      <p class="contact-line">
        <svg viewBox="0 0 10 10" aria-hidden="true"><rect x="0.5" y="2" width="9" height="6" fill="currentColor"/><path d="M0.5 2 L5 5.5 L9.5 2" fill="none" stroke="#f7f7f7" stroke-width="1"/></svg>
        lionel@bramblelearning.com.au
      </p>
    </div>

    <p class="brand-name">Bramble</p>

    <div class="company">
      <p class="company__name">Bramble Learning Works</p>
      <p class="company__address">1st Floor, 418 Ferncliff Road<br>Mt Dellmoor VIC 3187 Australia</p>
      <p class="contact-line">
        03 9512 4379
        <svg viewBox="0 0 10 10" aria-hidden="true"><path d="M2 1 L4 1 L4.8 3.4 L3.6 4.3 Q4.6 6 5.8 6.5 L6.7 5.3 L9 6.1 L9 8 Q8.5 9 7.5 9 Q1 8 1 2.3 Q1 1 2 1 Z" fill="currentColor"/></svg>
      </p>
      <p class="contact-line">
        www.bramblelearning.com.au
        <svg viewBox="0 0 10 10" aria-hidden="true"><circle cx="5" cy="5" r="4.5" fill="currentColor"/><path d="M0.5 5 H9.5 M5 0.5 Q2.5 5 5 9.5 M5 0.5 Q7.5 5 5 9.5" fill="none" stroke="#f7f7f7" stroke-width="0.7"/></svg>
      </p>
    </div>
  </section>

  <section class="card card--back" aria-label="Card back">
    <p class="back__brand">Bramble</p>
    <p class="back__tagline">Specialising in design and production of training</p>
    <p class="back__services">Video | Animation | Illustration | Text</p>
    <p class="back__delivery">for delivery via internet, intranet and/or LMS.</p>
    <div class="back__band"></div>
  </section>

</body>
</html>
```